A private security company called "Ventrell Security Services Ltd"

Hello everybody,

We need a web page for a company based in NZ. It is mainly an informative website so it would be wonderful if the designer puts their absolute best into making it a website that I would really appreciate. The website needs to show professionalism and also needs to make our web surfers find the information they need in a click. the company's colour is black and silver, and if those two colours could be integrated into the website it would be absolutely lovely. Please do contact me for any information.

Sincerely,
Dorian Valcourt

```html
<!DOCTYPE html>
<html lang="en">
<head>
<meta charset="utf-8">
<title>Ventrell Security Services Ltd</title>
<link rel="stylesheet" href="https://fonts.googleapis.com/css2?family=Montserrat:wght@500&family=Open+Sans:ital,wght@0,400;0,700;1,400&family=Sorts+Mill+Goudy&display=swap">
<style>
:root{
  --ink:#1f1f1f;
  --text:#333;
  --muted:#666;
  --silver:#bdbdbd;
  --line:#d4d4d4;
  --panel:#f1f1f1;
  --white:#fff;
  --nav-top:#444;
  --nav-bottom:#1e1e1e;
  --footer:#2c2c2c;
  --footer-text:#a9a9a9;
  --button:#333;
  --icon-dark:#2e2e2e;
  --icon-mid:#6d6d6d;
}
*{box-sizing:border-box;margin:0;padding:0}
html,body{width:1084px;height:1200px;overflow:hidden;background:var(--white)}
.page{position:relative;width:1200px;height:1328px;transform:scale(0.90333);transform-origin:0 0;font-family:"Open Sans",Arial,sans-serif;color:var(--text)}
.abs{position:absolute}

/* header */
.header{position:absolute;left:0;top:0;width:1200px;height:80px;background:var(--white)}
.contact-links{position:absolute;top:21px;left:100px;display:flex;gap:8px}
.contact-links span{width:33px;height:33px;border-radius:50%;display:flex;align-items:center;justify-content:center}
.contact-links span:nth-child(odd){background:var(--icon-dark)}
.contact-links span:nth-child(even){background:var(--icon-mid)}
.call{position:absolute;left:830px;top:24px}
.call svg{position:absolute;left:0;top:6px}
.call .label{position:absolute;left:40px;top:0;font-size:15px;color:#444;white-space:nowrap}
.call .number{position:absolute;left:40px;top:14px;font-size:26px;color:#5a5a5a;letter-spacing:-.5px;white-space:nowrap;font-family:Arial,sans-serif}

/* navigation */
.nav{position:absolute;left:0;top:80px;width:1200px;height:48px;background:linear-gradient(var(--nav-top),var(--nav-bottom))}
.nav a{position:absolute;top:0;line-height:48px;color:var(--white);font-family:"Montserrat",Arial,sans-serif;font-size:15.5px;text-decoration:none;transform:translateX(-50%);white-space:nowrap}
.nav i{position:absolute;top:8px;width:1px;height:32px;background:#6a6a6a}

.brand-badge{position:absolute;left:494px;top:15px;width:176px;height:176px;border-radius:50%;background:var(--white);border:3px solid #d6d6d6;display:flex;flex-direction:column;align-items:center;justify-content:center;z-index:2}
.brand-badge .name{font-family:"Montserrat",Arial,sans-serif;font-size:22px;letter-spacing:2px;color:var(--ink);margin-top:24px}
.brand-badge .sub{font-family:"Montserrat",Arial,sans-serif;font-size:9.5px;color:var(--ink);margin-top:2px}

/* hero */
.hero{position:absolute;left:0;top:128px;width:1200px;height:436px;
  background:
    radial-gradient(ellipse 260px 300px at 470px 250px,rgba(205,205,205,.55),rgba(205,205,205,0) 70%),
    radial-gradient(ellipse 200px 240px at 110px 320px,rgba(225,225,225,.45),rgba(225,225,225,0) 70%),
    radial-gradient(ellipse 380px 260px at 950px 200px,rgba(150,150,150,.45),rgba(150,150,150,0) 75%),
    radial-gradient(ellipse 300px 140px at 420px 430px,rgba(190,190,190,.4),rgba(190,190,190,0) 70%),
    linear-gradient(100deg,#2a2a2a 0%,#4a4a4a 22%,#3a3a3a 40%,#565656 62%,#3e3e3e 85%,#2b2b2b 100%);}

/* welcome */
.intro{position:absolute;left:0;top:564px;width:1200px;height:360px;background:var(--panel)}
.heading{font-family:"Sorts Mill Goudy",Georgia,serif;font-weight:400;color:var(--ink);white-space:nowrap}
.intro .heading{position:absolute;left:100px;top:50px;font-size:27px}
.intro-photo{position:absolute;left:103px;top:104px;width:183px;height:178px;border:3px solid #d8d8d8;background:linear-gradient(160deg,#d4d4d4,#8a8a8a 45%,#4a4a4a 75%,#6a6a6a)}
.intro-text{position:absolute;left:300px;top:103px;width:368px;font-family:Arial,sans-serif;font-size:12px;line-height:20px;color:#333}
.intro-text p+p{margin-top:20px}

.services{position:absolute;left:705px;top:42px;width:396px;height:259px;background:var(--white);border:1px solid var(--line)}
.services .heading{position:absolute;left:15px;top:14px;font-size:26px}
.services ul{position:absolute;left:0;top:52px;width:391px;list-style:none}
.services li{position:relative;height:38px;line-height:38px;padding-left:25px;font-size:14.5px;color:#333}
.services li::before{content:"";position:absolute;left:10px;top:15px;border-left:6px solid #aaa;border-top:4px solid transparent;border-bottom:4px solid transparent}
.services li.active{background:#dedede;border-left:2px solid #444;padding-left:23px}
.services li.active::before{left:8px;border-left-color:#333}

/* lower columns */
.lower{position:absolute;left:0;top:924px;width:1200px;height:308px;background:var(--white)}
.lower .heading{position:absolute;top:36px;font-size:27px}
.divider{position:absolute;top:44px;width:1px;height:200px;background:var(--line)}
.news-item{position:absolute;left:125px;width:263px}
.date{position:absolute;left:0;width:52px;height:52px;border-radius:50%;background:#ddd;text-align:center;font-style:italic;color:#222}
.date b{display:block;font-size:24px;line-height:26px;margin-top:5px}
.date small{display:block;font-size:12px;line-height:13px}
.news-item p{position:absolute;left:68px;width:200px;font-size:12px;line-height:20px;color:#555}
.news-item em{color:#888}
.button{position:absolute;height:26px;line-height:26px;padding:0 12px;background:var(--button);color:var(--white);font-weight:700;font-size:14px;border-radius:3px}
.quote{position:absolute;left:471px;top:86px;width:275px;font-style:italic;font-size:11.5px;line-height:20px;color:#555}
.quote-mark{position:absolute;font-family:Georgia,serif;font-size:34px;color:#888;line-height:1}
.author{position:absolute;right:534px;font-style:italic;text-align:right;white-space:nowrap}
.author-photo{position:absolute;left:675px;top:158px;width:80px;height:68px;border:2px solid #ddd;background:linear-gradient(#d0d0d0,#8a8a8a)}
.video{position:absolute;left:823px;top:82px;width:254px;height:182px;background:#1a1a1a;padding:4px}
.video .frame{width:100%;height:158px;background:radial-gradient(circle at 50% 50%,#9a9a9a,#5a5a5a 70%,#3a3a3a)}

/* footer */
.footer{position:absolute;left:0;top:1232px;width:1200px;height:96px;background:var(--footer)}
.footer-links{position:absolute;left:109px;top:25px;font-family:Arial,sans-serif;font-size:13px;color:var(--footer-text);word-spacing:2px;white-space:pre}
.copyright{position:absolute;left:109px;top:58px;font-family:Arial,sans-serif;font-size:11.5px;color:var(--footer-text);letter-spacing:.4px;white-space:nowrap}
.footer-brand{position:absolute;right:112px;top:52px;text-align:center;color:#ddd;font-family:"Montserrat",Arial,sans-serif}
.footer-brand .name{font-size:17px;letter-spacing:1.5px}
.footer-brand .sub{font-size:8.5px}
</style>
</head>
<body>
<div class="page">

  <header class="header">
    <div class="contact-links" aria-label="Quick contact links">
      <span><svg width="16" height="16" viewBox="0 0 24 24" aria-hidden="true"><path fill="#fff" d="M6.6 10.8a15.1 15.1 0 0 0 6.6 6.6l2.2-2.2c.3-.3.7-.4 1-.2 1.1.4 2.3.6 3.6.6.6 0 1 .4 1 1V20c0 .6-.4 1-1 1A17 17 0 0 1 3 4c0-.6.4-1 1-1h3.5c.6 0 1 .4 1 1 0 1.3.2 2.5.6 3.6.1.3 0 .7-.2 1z"/></svg></span>
      <span><svg width="16" height="16" viewBox="0 0 24 24" aria-hidden="true"><path fill="#fff" d="M12 2a7 7 0 0 0-7 7c0 5 7 13 7 13s7-8 7-13a7 7 0 0 0-7-7zm0 9.5A2.5 2.5 0 1 1 12 6.5a2.5 2.5 0 0 1 0 5z"/></svg></span>
      <span><svg width="16" height="16" viewBox="0 0 24 24" aria-hidden="true"><path fill="none" stroke="#fff" stroke-width="2.6" stroke-linecap="round" stroke-linejoin="round" d="M5 12.5l4.5 4.5L19 7"/></svg></span>
      <span><svg width="16" height="16" viewBox="0 0 24 24" aria-hidden="true"><rect x="3" y="6" width="18" height="12" rx="1" fill="#fff"/><path d="M3.5 6.5L12 13l8.5-6.5" fill="none" stroke="#6d6d6d" stroke-width="1.6"/></svg></span>
    </div>
    <div class="call">
      <svg width="30" height="30" viewBox="0 0 24 24" aria-hidden="true"><path fill="#6a6a6a" d="M6.6 10.8a15.1 15.1 0 0 0 6.6 6.6l2.2-2.2c.3-.3.7-.4 1-.2 1.1.4 2.3.6 3.6.6.6 0 1 .4 1 1V20c0 .6-.4 1-1 1A17 17 0 0 1 3 4c0-.6.4-1 1-1h3.5c.6 0 1 .4 1 1 0 1.3.2 2.5.6 3.6.1.3 0 .7-.2 1z"/></svg>
      <div class="label">Call Now Today</div>
      <div class="number">+64 (09) 415-27-80</div>
    </div>
  </header>

  <nav class="nav">
    <a style="left:152px">HOME</a><i style="left:210px"></i>
    <a style="left:269px">ABOUT</a><i style="left:330px"></i>
    <a style="left:402px">SERVICES</a><i style="left:472px"></i>
    <i style="left:688px"></i><a style="left:745px">SECURITY</a>
    <i style="left:822px"></i><a style="left:881px">BLOG</a>
    <i style="left:933px"></i><a style="left:1020px">CONTACT US</a>
  </nav>

  <div class="brand-badge">
    <div class="name">VENTRELL</div>
    <div class="sub">Security Services Ltd.</div>
  </div>

  <div class="hero" role="img" aria-label="Black and white photograph of uniformed security officers in berets against foliage"></div>

  <section class="intro">
    <h1 class="heading">Welcome to Ventrell Security Services Ltd.</h1>
    <div class="intro-photo" role="img" aria-label="Photograph of two uniformed officers in training"></div>
    <div class="intro-text">
      <p>Lorem ipsum dolor sit amet, consectetur adipiscing elit. Quisque dapibus accumsan orci, pretium eleifend arcu adipiscing eget. Fusce accumsan facilisis tincidunt. Phasellus tempor enim purus, vitae venenatis est. Ut imperdiet hendrerit pulvinar. Cras at tellus a enim condimentum mollis ut et tellus.</p>
      <p>Mauris dolor magna, elementum eu dictum eu, fermentum a nibh. Praesent ut dui lectus, vel lacinia sem. Praesent commodo male-suada urna, quis convallis risus dictum et.</p>
    </div>
    <aside class="services">
      <h2 class="heading">The services i provide are:</h2>
      <ul>
        <li>Property guards</li>
        <li class="active">Corporate events security</li>
        <li>personal bodyguard for high net worth individuals</li>
        <li>security consultancy</li>
        <li>private investigation</li>
      </ul>
    </aside>
  </section>

  <section class="lower">
    <h2 class="heading" style="left:123px">Update News</h2>
    <div class="news-item" style="top:84px">
      <div class="date"><b>25</b><small>Nov</small></div>
      <p style="top:-4px">Aliquam molestie, mi et imperdiet euismod, dui purus auctor tellus, et interdum lacus.. <em>Read More</em></p>
    </div>
    <div class="abs" style="left:125px;top:148px;width:263px;height:1px;background:var(--line)"></div>
    <div class="news-item" style="top:161px">
      <div class="date"><b>20</b><small>Nov</small></div>
      <p style="top:-4px">Aliquam molestie, mi et imperdiet euismod, dui purus auctor tellus, et interdum lacus.. <em>Read More</em></p>
    </div>
    <div class="button" style="left:308px;top:232px">Read All</div>

    <div class="divider" style="left:438px"></div>

    <h2 class="heading" style="left:470px">Testimonials</h2>
    <div class="quote-mark" style="left:475px;top:84px">&ldquo;</div>
    <p class="quote"><span style="padding-left:36px"></span>Suspendisse lobortis turpis in odio blandit ac interdum lorem euismod. Aenean a nibh eget turpis vehicula tempus ac sed massa.....</p>
    <div class="quote-mark" style="left:650px;top:128px">&rdquo;</div>
    <div class="author" style="top:190px;font-size:12px;color:#222">By Colin Harte</div>
    <div class="author" style="top:211px;font-size:10.5px;color:#777">Posted on Nov25, 2012</div>
    <div class="author-photo" role="img" aria-label="Portrait photograph of the client"></div>
    <div class="button" style="left:673px;top:238px">Read All</div>

    <div class="divider" style="left:788px"></div>

    <h2 class="heading" style="left:823px">Watch Videos</h2>
    <div class="video">
      <div class="frame" role="img" aria-label="Video still of a large group of uniformed officers"></div>
      <svg class="abs" style="left:104px;top:56px" width="54" height="54" viewBox="0 0 54 54" aria-hidden="true">
        <circle cx="27" cy="27" r="25" fill="#222" stroke="#eee" stroke-width="3"/>
        <path d="M21 16 L38 27 L21 38Z" fill="#fff"/>
      </svg>
      <svg class="abs" style="left:4px;top:166px" width="246" height="12" viewBox="0 0 246 12" aria-hidden="true">
        <path d="M4 3 L10 6 L4 9Z" fill="#ddd"/>
        <rect x="16" y="5" width="150" height="2" fill="#666"/>
        <rect x="200" y="3" width="10" height="6" fill="#999"/>
        <rect x="222" y="5" width="16" height="2" fill="#ccc"/>
      </svg>
    </div>
  </section>

  <footer class="footer">
    <div class="footer-links">HOME    |    ABOUT    |    SERVICES    |    BLOG    |    CONTACT US</div>
    <div class="copyright">© 2014 . All right reserved. Privacy Policy | Terms &amp; Conditions</div>
    <div class="footer-brand">
      <div class="name">VENTRELL</div>
      <div class="sub">Security Services Ltd.</div>
    </div>
  </footer>

</div>
</body>
</html>
```